Korvell Plant Services

We are a heavy diesel mechanical business with additional air con certificates, remapping engine rebuilt

Contact Information for Business Card

Company Name, Director Name, Managing Director, Contact details, email and website

Font styles to use
Serif
Script

```html
<!DOCTYPE html>
<html lang="en">
<head>
<meta charset="utf-8">
<title>Korvell Plant Services – Business Card</title>
<link href="https://fonts.googleapis.com/css2?family=Arimo:wght@400;700&display=swap" rel="stylesheet">
<style>
  :root {
    --bg: #7d7d7d;
    --card-dark: #000000;
    --card-light: #f4f4f6;
    --navy: #1b1f6e;
    --ink: #2a2a2a;
    --muted: #555555;
    --rule: #3a3a3a;
    --white: #ffffff;
  }
  * { box-sizing: border-box; margin: 0; padding: 0; }
  html, body {
    width: 1200px; height: 900px; overflow: hidden;
    background: var(--bg);
    font-family: "Arimo", Arial, sans-serif;
  }
  .stage {
    position: relative; width: 1200px; height: 900px;
    display: flex; flex-direction: column; align-items: center; justify-content: center; gap: 50px;
  }
  .card {
    position: relative; width: 600px; height: 343px;
    border-radius: 22px; overflow: hidden;
  }
  .card--front {
    background: var(--card-dark);
    display: flex; align-items: center; justify-content: center;
  }
  .card--back {
    background: var(--card-light);
    border-bottom: 3px solid var(--navy);
  }
  .brand {
    display: flex; align-items: center; gap: 14px;
    font-weight: 700; line-height: 1.05;
  }
  .brand__dot {
    width: 22px; height: 22px; border-radius: 50%; flex: none;
  }
  .card--front .brand { color: var(--white); font-size: 34px; }
  .card--front .brand__dot { background: var(--white); }
  .card--back .brand {
    position: absolute; left: 40px; top: 78px;
    color: var(--navy); font-size: 25px;
  }
  .card--back .brand__dot { background: var(--navy); width: 16px; height: 16px; }
  .divider {
    position: absolute; left: 250px; right: 0; top: 190px;
    height: 1px; background: var(--rule);
  }
  .contact {
    position: absolute; right: 40px; top: 44px; width: 230px;
    text-align: right;
  }
  .contact__name { color: var(--navy); font-weight: 700; font-size: 23px; }
  .contact__role { color: var(--muted); font-size: 15px; margin-top: 2px; padding-bottom: 8px; border-bottom: 1px solid var(--rule); }
  .contact__list { list-style: none; margin-top: 10px; }
  .contact__item {
    display: flex; justify-content: flex-end; align-items: center; gap: 6px;
    color: var(--ink); font-size: 15px; line-height: 1.45;
  }
  .contact__item svg { width: 12px; height: 12px; fill: var(--navy); flex: none; }
  .address {
    position: absolute; left: 40px; bottom: 46px;
    border-top: 1px solid var(--rule); padding-top: 12px; width: 240px;
    color: var(--ink); font-size: 16px; line-height: 1.3;
  }
</style>
</head>
<body>
<main class="stage">
  <section class="card card--front" aria-label="Card front">
    <div class="brand"><span class="brand__dot"></span><span>Korvell<br>Plant Services</span></div>
  </section>

  <section class="card card--back" aria-label="Card back">
    <div class="brand"><span class="brand__dot"></span><span>Korvell<br>Plant Services</span></div>
    <div class="divider"></div>
    <div class="contact">
      <p class="contact__name">Tomas Renwick</p>
      <p class="contact__role">Managing Director</p>
      <ul class="contact__list">
        <li class="contact__item">(555) 0147-3920
          <svg viewBox="0 0 24 24"><path d="M6.6 10.8a15.1 15.1 0 0 0 6.6 6.6l2.2-2.2c.3-.3.7-.4 1-.2 1.1.4 2.3.6 3.6.6.6 0 1 .4 1 1V20c0 .6-.4 1-1 1A17 17 0 0 1 3 4c0-.6.4-1 1-1h3.5c.6 0 1 .4 1 1 0 1.3.2 2.5.6 3.6.1.3 0 .7-.2 1z"/></svg>
        </li>
        <li class="contact__item">name@korvell.com
          <svg viewBox="0 0 24 24"><path d="M2 5h20v14H2z M2 5l10 8 10-8" /></svg>
        </li>
        <li class="contact__item">www.korvell.com
          <svg viewBox="0 0 24 24"><circle cx="12" cy="12" r="10"/></svg>
        </li>
      </ul>
    </div>
    <p class="address">2917 Ashgrove Lane<br>Millbrook, NY 12545</p>
  </section>
</main>
</body>
</html>
```